Travel Group 'Lydgate Group' needs a new business card design

Lydgate Group is a diverse business specialising in bespoke, tailor made holidays to suit all budgets and we are specialists in planning exciting day/short trips to suit all markets. Our target market is very varied going from the corporate client and as well as people in the community who simply want to experience something special.
We are looking for a card design that will encourage people to look at our websites and social media platforms and to see for themselves the different facets to our business. It is essential that the card has social media icons for Facebook, Twitter and Instagram. We are looking for a card with a blank background with no pictures and for the front side to have the attached Lydgate logo. The card should have similar colour scheme to the attached Lydgate logo.
The card must have the following information on one side:
Maud Penrose
Business Development Manager
maudpenrose@lydgatevoyages.example
Lydgate Group, 87 Quarry Lane
Kilwinning, Ayrshire, Scotland KA19 4TN
+44 (0)1294 730182
And then the card must have the following on the second side:
(Lydgate logo)
(social media icons)
www.lydgatevoyages.example
www.lydgateoutings.example
Target Market(s)
Our target market is very varied going from the corporate client and as well as people in the community who simply want to experience something special.
Industry/Entity Type
Business
Contact Information for Business Card
Maud Penrose
+44 (0)1294 730182
(Lydgate logo)
(social media icons)
www.lydgatevoyages.example
www.lydgateoutings.example
Requirements
Must have
- It is essential that the card has social media icons for Facebook, Twitter & Instagram.
Should not have
- Should not have any images other than Lydgate logo.

```html
<!DOCTYPE html>
<html lang="en">
<head>
<meta charset="utf-8">
<title>Lydgate Group – Business Card</title>
<link rel="stylesheet" href="https://fonts.googleapis.com/css2?family=Work+Sans:wght@400;500;600&display=swap">
<style>
  :root {
    --backdrop: #2b2b2b;
    --card: #1e1e1f;
    --pink: #e22a92;
    --violet: #3a2b8c;
    --white: #f2f2f2;
    --muted: #d9d9d9;
  }
  html, body {
    margin: 0;
    width: 1200px;
    height: 900px;
    overflow: hidden;
    background: var(--backdrop);
    font-family: "Work Sans", Arial, sans-serif;
  }
  .sheet {
    position: relative;
    width: 1200px;
    height: 900px;
  }
  .card {
    position: absolute;
    left: 250px;
    width: 700px;
    height: 390px;
    background: var(--card);
    box-shadow: 0 10px 30px rgba(0,0,0,.45);
    overflow: hidden;
  }
  .card--front { top: 40px; }
  .card--back  { top: 470px; }

  /* Front */
  .front-brand {
    position: absolute;
    top: 120px;
    left: 0;
    width: 100%;
    text-align: center;
    font-size: 52px;
    font-weight: 600;
    letter-spacing: 6px;
    color: var(--white);
  }
  .social {
    position: absolute;
    top: 232px;
    left: 0;
    width: 100%;
    display: flex;
    justify-content: center;
    gap: 14px;
  }
  .social-dot {
    width: 24px;
    height: 24px;
    border-radius: 50%;
    background: var(--pink);
  }
  .front-web {
    position: absolute;
    top: 278px;
    left: 0;
    width: 100%;
    text-align: center;
    font-size: 17px;
    letter-spacing: 1.5px;
    color: var(--white);
  }

  /* Back */
  .back-brand {
    position: absolute;
    top: 165px;
    left: 30px;
    width: 270px;
    text-align: center;
    font-size: 40px;
    font-weight: 600;
    letter-spacing: 4px;
    color: var(--violet);
  }
  .divider {
    position: absolute;
    left: 318px;
    top: 70px;
    width: 3px;
    height: 230px;
    background: var(--pink);
  }
  .details {
    position: absolute;
    left: 342px;
    top: 66px;
    width: 334px;
    color: var(--white);
    font-size: 15px;
    line-height: 1.3;
    white-space: nowrap;
  }
  .details p { margin: 0; }
  .person-name {
    font-size: 25px;
    font-weight: 600;
    letter-spacing: 1.5px;
    color: var(--pink);
    text-transform: uppercase;
  }
  .details .person-role { margin: 2px 0 10px; font-size: 17px; }
  .company {
    font-weight: 500;
    letter-spacing: 1px;
    color: var(--pink);
    text-transform: uppercase;
  }
  .details .address { margin-bottom: 12px; }
  .contact-list { list-style: none; margin: 0; padding: 0; }
  .contact-list li {
    display: flex;
    align-items: center;
    gap: 10px;
    margin-bottom: 4px;
  }
  .contact-list svg { width: 15px; height: 15px; fill: var(--pink); flex: none; }
  .accent { color: var(--pink); }
</style>
</head>
<body>
<main class="sheet">
  <section class="card card--front" aria-label="Card front">
    <div class="front-brand">LYDGATE</div>
    <div class="social" aria-label="Social media links">
      <span class="social-dot"></span>
      <span class="social-dot"></span>
      <span class="social-dot"></span>
    </div>
    <div class="front-web">www.lydgateoutings.example</div>
  </section>

  <section class="card card--back" aria-label="Card back">
    <div class="back-brand">LYDGATE</div>
    <div class="divider"></div>
    <div class="details">
      <p class="person-name">Maud Penrose</p>
      <p class="person-role">Business Development Manager</p>
      <p class="company">Lydgate Group,</p>
      <p class="address">87 Quarry Lane Kilwinning,<br>Ayrshire, Scotland KA19 4TN</p>
      <ul class="contact-list">
        <li>
          <svg viewBox="0 0 24 24" aria-hidden="true"><path d="M6.6 10.8a15.1 15.1 0 0 0 6.6 6.6l2.2-2.2a1 1 0 0 1 1-.25 11.4 11.4 0 0 0 3.6.6 1 1 0 0 1 1 1V20a1 1 0 0 1-1 1A17 17 0 0 1 3 4a1 1 0 0 1 1-1h3.5a1 1 0 0 1 1 1c0 1.25.2 2.45.6 3.6a1 1 0 0 1-.25 1z"/></svg>
          +44 (0)1294 730182
        </li>
        <li>
          <svg viewBox="0 0 24 24" aria-hidden="true"><path d="M2 5h20v14H2z M3 6l9 7 9-7" fill="none" stroke="#e22a92" stroke-width="2"/></svg>
          maudpenrose@lydgatevoyages.example
        </li>
        <li>
          <svg viewBox="0 0 24 24" aria-hidden="true"><g fill="none" stroke="#e22a92" stroke-width="1.8"><circle cx="12" cy="12" r="9"/><ellipse cx="12" cy="12" rx="4" ry="9"/><path d="M3 12h18M5 7h14M5 17h14"/></g></svg>
          <span>www.<span class="accent">lydgatevoyages</span>.example</span>
        </li>
      </ul>
    </div>
  </section>
</main>
</body>
</html>
```